Willowmere Spa and Beauty Ltd. (Name of business)

I need a business card designed for this new company based out of Toronto Ontario. We specialize in Eyelash Extensions, Manicures and Pedicures, body waxing, massages, laser hair removal and botox treatments. Also offer a variety of products for sale, such as skin cream serums, collagen gel, eye cream, etc. It is a safe relaxing and non-judgemental environnment. Clients are welcome to come be pampered for the half or full day. Many service packages to choose from.

Open 7days per week from 8am to 8pm.

Marissa Thornbury
Spa Facilitator
Willowmere Spa and Beauty Ltd.
7200 Calder Ave; Suite 1400
Toronto ON K8P 2W7

OFFICE: 416.739.4100
FAX: 416.739.4101
CELL: 416.582.6074
EMAIL: marissa.thornbury@willowmerespa.example

Target Market(s)

Target market is primarily female ranging from 16 years old to 50 years old.

Industry/Entity Type

Business

Contact Information for Business Card

Marissa Thornbury
Spa Facilitator
7200 Calder Ave; Suite 1400
Toronto ON K8P 2W7

OFFICE: 416.739.4100
FAX: 416.739.4101
CELL: 416.582.6074

Logo Text

I dont have a logo yet. I would like it simple but sophisticated and modern.

Font styles to use
Serif

Requirements
Must have
• all pertinent details such as company name, logo, name and contact information, services that are offered, including package rates
Nice to have
• Company name and logo prominent. A card that is neat and the information such as address, phone number, fax, email, etc is not too crowded but laid out in an easy to read format.
• Possibly on the back of card - some of the services offered could be listed, as well as professional cream lotions and serums. Hours of operation etc.

```html
<!DOCTYPE html>
<html lang="en">
<head>
<meta charset="utf-8">
<title>Willowmere Spa and Beauty Ltd. — Business Card</title>
<link rel="stylesheet" href="https://fonts.googleapis.com/css2?family=Lato:wght@300;400&display=swap">
<style>
  :root {
    --canvas: #e9e6e1;
    --rose: #c81e50;
    --rose-deep: #a8163f;
    --ink: #1b1b1d;
    --ink-soft: #2a2a2d;
    --white: #ffffff;
    --white-soft: #f4dbe2;
  }
  * { margin: 0; padding: 0; box-sizing: border-box; }
  html, body { width: 771px; height: 1200px; overflow: hidden; }
  body {
    background: var(--canvas);
    font-family: "Lato", "Helvetica Neue", Arial, sans-serif;
    font-weight: 300;
    position: relative;
  }
  .card {
    position: absolute;
    left: 65px;
    width: 641px;
    height: 366px;
    border-radius: 4px;
    box-shadow: 0 6px 18px rgba(0,0,0,0.18);
    overflow: hidden;
  }
  .card--front { top: 180px; background: linear-gradient(160deg, var(--rose) 0%, var(--rose-deep) 100%); color: var(--white); }
  .card--back  { top: 620px; background: linear-gradient(160deg, var(--ink-soft) 0%, var(--ink) 100%); color: var(--white); }

  /* brand block */
  .brand {
    position: absolute;
    display: flex;
    align-items: center;
    gap: 14px;
  }
  .brand__dot {
    width: 46px; height: 46px; border-radius: 50%;
    flex: none;
  }
  .brand__name {
    font-weight: 300;
    font-size: 22px;
    letter-spacing: 4px;
    line-height: 1.25;
    text-transform: uppercase;
  }
  .card--front .brand { right: 40px; top: 70px; }
  .card--front .brand__dot { background: var(--white); }
  .card--front .brand__name { color: var(--white); }
  .card--back .brand { right: 40px; top: 36px; }
  .card--back .brand__dot { background: var(--rose); }
  .card--back .brand__name { color: var(--white); }

  /* holder */
  .holder {
    position: absolute;
    left: 40px; top: 160px;
    padding-left: 16px;
    border-left: 4px solid var(--white);
  }
  .holder__name { font-size: 30px; font-weight: 300; letter-spacing: 1px; }
  .holder__title { font-size: 19px; font-weight: 400; color: var(--white-soft); margin-top: 2px; }

  /* contact */
  .contact {
    position: absolute;
    right: 40px; bottom: 30px;
    list-style: none;
    font-size: 14px;
    font-weight: 400;
    line-height: 1.5;
  }
  .contact__item { display: flex; align-items: flex-start; gap: 10px; }
  .contact__icon { width: 14px; height: 14px; margin-top: 3px; flex: none; fill: var(--white); }

  /* services */
  .services {
    position: absolute;
    left: 40px; top: 108px;
    font-size: 14px;
    font-weight: 400;
    line-height: 1.4;
  }
  .services__heading {
    color: var(--rose);
    font-size: 14px;
    font-weight: 400;
    margin-top: 4px;
  }
  .services__heading:first-child { margin-top: 0; }
  .services__list { list-style: none; }
  .services__item { display: flex; align-items: center; gap: 8px; }
  .services__tick { width: 12px; height: 12px; flex: none; }
  .services__tick rect { fill: var(--rose); }
  .services__tick path { stroke: var(--white); stroke-width: 2; fill: none; }

  .hours {
    position: absolute;
    right: 40px; bottom: 28px;
    color: var(--rose);
    font-size: 14px;
    font-weight: 400;
  }
</style>
</head>
<body>

<section class="card card--front" aria-label="Business card front">
  <div class="brand">
    <span class="brand__dot"></span>
    <p class="brand__name">Willowmere<br>Spa and Beauty Ltd.</p>
  </div>

  <div class="holder">
    <h1 class="holder__name">Marissa Thornbury</h1>
    <p class="holder__title">Spa Facilitator</p>
  </div>

  <ul class="contact">
    <li class="contact__item">
      <svg class="contact__icon" viewBox="0 0 14 14" aria-hidden="true"><path d="M7 0a5 5 0 0 0-5 5c0 4 5 9 5 9s5-5 5-9a5 5 0 0 0-5-5zm0 7a2 2 0 1 1 0-4 2 2 0 0 1 0 4z"/></svg>
      <span>7200 Calder Ave; Suite 1400<br>Toronto ON K8P 2W7</span>
    </li>
    <li class="contact__item">
      <svg class="contact__icon" viewBox="0 0 14 14" aria-hidden="true"><path d="M3 1l2 3-1.5 1.5a8 8 0 0 0 5 5L10 9l3 2-1 2.5C6 13.5.5 8 .5 2z"/></svg>
      <span>416.739.4100</span>
    </li>
    <li class="contact__item">
      <svg class="contact__icon" viewBox="0 0 14 14" aria-hidden="true"><path d="M3 1h6v3H3zM1 5h12v7H1zm2 2v1h8V7z"/></svg>
      <span>416.739.4101</span>
    </li>
    <li class="contact__item">
      <svg class="contact__icon" viewBox="0 0 14 14" aria-hidden="true"><path d="M4 0h6a1 1 0 0 1 1 1v12a1 1 0 0 1-1 1H4a1 1 0 0 1-1-1V1a1 1 0 0 1 1-1zm0 2v9h6V2z"/></svg>
      <span>416.582.6074</span>
    </li>
    <li class="contact__item">
      <svg class="contact__icon" viewBox="0 0 14 14" aria-hidden="true"><path d="M0 3h14v9H0zm1.5 1L7 8l5.5-4z"/></svg>
      <span>marissa.thornbury@willowmerespa.example</span>
    </li>
  </ul>
</section>

<section class="card card--back" aria-label="Business card back">
  <div class="brand">
    <span class="brand__dot"></span>
    <p class="brand__name">Willowmere<br>Spa and Beauty Ltd.</p>
  </div>

  <div class="services">
    <h2 class="services__heading">We specialize in</h2>
    <ul class="services__list">
      <li class="services__item"><svg class="services__tick" viewBox="0 0 13 13" aria-hidden="true"><rect width="13" height="13" rx="1"/><path d="M3 6.5l2.5 2.5L10 3.5"/></svg>Eyelash Extensions</li>
      <li class="services__item"><svg class="services__tick" viewBox="0 0 13 13" aria-hidden="true"><rect width="13" height="13" rx="1"/><path d="M3 6.5l2.5 2.5L10 3.5"/></svg>Manicures and Pedicures</li>
      <li class="services__item"><svg class="services__tick" viewBox="0 0 13 13" aria-hidden="true"><rect width="13" height="13" rx="1"/><path d="M3 6.5l2.5 2.5L10 3.5"/></svg>body waxing</li>
      <li class="services__item"><svg class="services__tick" viewBox="0 0 13 13" aria-hidden="true"><rect width="13" height="13" rx="1"/><path d="M3 6.5l2.5 2.5L10 3.5"/></svg>massages</li>
      <li class="services__item"><svg class="services__tick" viewBox="0 0 13 13" aria-hidden="true"><rect width="13" height="13" rx="1"/><path d="M3 6.5l2.5 2.5L10 3.5"/></svg>laser hair removal and botox treatments</li>
    </ul>
    <h2 class="services__heading">We offer variety of products for sale</h2>
    <ul class="services__list">
      <li class="services__item"><svg class="services__tick" viewBox="0 0 13 13" aria-hidden="true"><rect width="13" height="13" rx="1"/><path d="M3 6.5l2.5 2.5L10 3.5"/></svg>skin cream serums</li>
      <li class="services__item"><svg class="services__tick" viewBox="0 0 13 13" aria-hidden="true"><rect width="13" height="13" rx="1"/><path d="M3 6.5l2.5 2.5L10 3.5"/></svg>collagen gel</li>
      <li class="services__item"><svg class="services__tick" viewBox="0 0 13 13" aria-hidden="true"><rect width="13" height="13" rx="1"/><path d="M3 6.5l2.5 2.5L10 3.5"/></svg>eye cream,</li>
    </ul>
  </div>

  <p class="hours">Open 7days per week from 8am to 8pm</p>
</section>

</body>
</html>
```